Business Card Design Project

I help solve problems that people have with real estate, so I buy homes for cash that they no longer want, can't afford, inherited, etc. and fix and sell them or rent them or take over mortgage payments. See website: www.quickhomepurchase-example.com

Industry/Entity Type

Real Estate

Contact Information for Business Card

Not exactly sure. Looking for a design that either is similar to the website www.quickhomepurchase-example.com or that reflects what I do as described below. If it can look a little luxurious to show I can buy the houses for cash and I fix them and sell them, it's a bonus. I seem to like some of the higher end things like foil or black or something that makes it stand out.

Font styles to use
Serif

Requirements
Nice to have
• I seem to like black or clear. I like things to stand out and be different.

```html
<!DOCTYPE html>
<html lang="en">
<head>
<meta charset="utf-8">
<title>Renewed Residences – Business Cards</title>
<link href="https://fonts.googleapis.com/css2?family=Lato:wght@400;900&display=swap" rel="stylesheet">
<style>
  :root {
    --backdrop: #44445f;
    --card-white: #ffffff;
    --green-light: #8cc63f;
    --green-mid: #62a43c;
    --green-dark: #468535;
    --brand-green: #3f8a2e;
    --ink: #1e2a1a;
    --ink-soft: #2b3a24;
    --white: #ffffff;
  }
  * { margin: 0; padding: 0; box-sizing: border-box; }
  html, body { width: 1200px; height: 1000px; overflow: hidden; }
  body {
    background: var(--backdrop);
    font-family: "Lato", Arial, sans-serif;
    position: relative;
  }
  .card {
    position: absolute;
    width: 512px;
    height: 292px;
  }
  .card--rounded { border-radius: 30px; }
  .card--front { background: var(--card-white); }
  .card--back {
    background: linear-gradient(90deg, var(--green-light) 0%, var(--green-mid) 55%, var(--green-dark) 100%);
    color: var(--ink);
  }
  .card-a { left: 66px; top: 101px; }
  .card-b { left: 66px; top: 449px; }
  .card-c { left: 625px; top: 266px; border-radius: 0; }
  .card-d { left: 624px; top: 607px; border-radius: 0; }

  .front-brand {
    position: absolute;
    inset: 0;
    display: flex;
    flex-direction: column;
    align-items: center;
    justify-content: center;
    text-align: center;
    color: var(--brand-green);
    font-weight: 900;
    font-size: 50px;
    line-height: 1.05;
    letter-spacing: 1px;
    text-transform: uppercase;
  }

  .back-brand {
    position: absolute;
    left: 27px;
    top: 30px;
    color: var(--white);
    font-weight: 900;
    font-size: 19px;
    line-height: 1.05;
    letter-spacing: 0.5px;
    text-transform: uppercase;
  }
  .person-name {
    position: absolute;
    left: 27px;
    top: 96px;
    font-size: 25px;
    font-weight: 400;
    color: var(--ink);
  }
  .person-title {
    position: absolute;
    left: 27px;
    top: 132px;
    font-size: 14px;
    color: var(--ink-soft);
  }
  .divider {
    position: absolute;
    left: 27px;
    top: 162px;
    width: 232px;
    height: 2px;
    background: var(--ink);
  }
  .contact-list {
    position: absolute;
    left: 27px;
    top: 193px;
    list-style: none;
  }
  .contact-item {
    display: flex;
    align-items: center;
    height: 24px;
    font-size: 17px;
    color: var(--ink);
  }
  .contact-icon {
    width: 14px;
    height: 14px;
    margin-right: 20px;
    fill: var(--ink);
  }
  .website {
    position: absolute;
    right: 33px;
    bottom: 24px;
    font-size: 14px;
    color: var(--ink);
  }
</style>
</head>
<body>

  <section class="card card--rounded card--front card-a">
    <div class="front-brand">Renewed<br>Residences</div>
  </section>

  <section class="card card--rounded card--back card-b">
    <div class="back-brand">Renewed<br>Residences</div>
    <div class="person-name">Name of Person</div>
    <div class="person-title">Title of Person</div>
    <div class="divider"></div>
    <ul class="contact-list">
      <li class="contact-item">
        <svg class="contact-icon" viewBox="0 0 24 24"><path d="M6.6 10.8a15.1 15.1 0 0 0 6.6 6.6l2.2-2.2c.3-.3.7-.4 1-.2 1.1.4 2.3.6 3.6.6.6 0 1 .4 1 1V20c0 .6-.4 1-1 1A17 17 0 0 1 3 4c0-.6.4-1 1-1h3.5c.6 0 1 .4 1 1 0 1.3.2 2.5.6 3.6.1.3 0 .7-.2 1z"/></svg>
        +123 456 7890
      </li>
      <li class="contact-item">
        <svg class="contact-icon" viewBox="0 0 24 24"><path d="M2 5h20v14H2z M2 5l10 8 10-8" stroke="#8cc63f" stroke-width="1.5"/></svg>
        E-mail Address
      </li>
    </ul>
    <div class="website">www.quickhomepurchase-example.com</div>
  </section>

  <section class="card card--front card-c">
    <div class="front-brand">Renewed<br>Residences</div>
  </section>

  <section class="card card--back card-d">
    <div class="back-brand">Renewed<br>Residences</div>
    <div class="person-name">Name of Person</div>
    <div class="person-title">Title of Person</div>
    <div class="divider"></div>
    <ul class="contact-list">
      <li class="contact-item">
        <svg class="contact-icon" viewBox="0 0 24 24"><path d="M6.6 10.8a15.1 15.1 0 0 0 6.6 6.6l2.2-2.2c.3-.3.7-.4 1-.2 1.1.4 2.3.6 3.6.6.6 0 1 .4 1 1V20c0 .6-.4 1-1 1A17 17 0 0 1 3 4c0-.6.4-1 1-1h3.5c.6 0 1 .4 1 1 0 1.3.2 2.5.6 3.6.1.3 0 .7-.2 1z"/></svg>
        +123 456 7890
      </li>
      <li class="contact-item">
        <svg class="contact-icon" viewBox="0 0 24 24"><path d="M2 5h20v14H2z M2 5l10 8 10-8" stroke="#8cc63f" stroke-width="1.5"/></svg>
        E-mail Address
      </li>
    </ul>
    <div class="website">www.quickhomepurchase-example.com</div>
  </section>

</body>
</html>
```